red quince
silk in motion
Modern
Dunmore Court
Harbor & Vale
Carmel, CA 93921
info@red-quince-shop.com
www.red-quince-shop.com
I'd like the card to be vertical, not horizontal! The logo should be centered!!!
should be the same, except the address:
P.O.Box 4819
Carmel, CA 93921-4819
logo should be centered on a vertical double sided business card!

```html
<!DOCTYPE html>
<html lang="en">
<head>
<meta charset="utf-8">
<title>red quince — stationery set</title>
<link href="https://fonts.googleapis.com/css2?family=Open+Sans:wght@400;600&display=swap" rel="stylesheet">
<style>
  :root {
    --stage: #2b2c2e;
    --stage-dark: #1f2022;
    --navy: #163a7c;
    --sky: #29a6dc;
    --brand-blue: #3f9fd8;
    --paper: #ffffff;
    --paper-shade: #eef1f4;
    --ink: #4a5563;
    --label: #8a8f96;
    --watermark: #dcebf6;
  }
  * { margin: 0; padding: 0; box-sizing: border-box; }
  html, body { width: 1200px; height: 384px; overflow: hidden; }
  body {
    background: radial-gradient(ellipse at 50% 40%, var(--stage) 0%, var(--stage-dark) 100%);
    font-family: "Open Sans", Arial, sans-serif;
    position: relative;
  }
  .piece { position: absolute; box-shadow: 0 2px 6px rgba(0,0,0,.45); }
  .label {
    position: absolute; font-size: 6px; color: var(--label);
    text-align: center; letter-spacing: .2px;
  }

  /* wordmark: name set plainly in the text font */
  .wordmark {
    font-family: "Open Sans", Arial, sans-serif; font-weight: 600;
    text-transform: uppercase; letter-spacing: .12em;
    line-height: 1; white-space: nowrap; text-align: center;
  }

  /* business cards */
  .card { width: 62px; height: 120px; display: flex; flex-direction: column; align-items: center; }
  .card--white { background: var(--paper); color: var(--brand-blue); }
  .card--navy { background: var(--navy); color: var(--paper); }
  .card--sky { background: var(--sky); color: var(--paper); }
  .card .wordmark { margin-top: 16px; font-size: 6px; }
  .card-tagline { font-size: 3.5px; margin-top: 3px; letter-spacing: .4px; }
  .card-details { margin-top: auto; margin-bottom: 8px; font-size: 3.2px; line-height: 1.5; text-align: center; color: var(--ink); }
  .card--navy .card-details { color: var(--paper); }
  .card--centered { justify-content: center; }
  .card--centered .wordmark { margin-top: 0; }

  /* letterheads */
  .letterhead { width: 245px; height: 326px; background: var(--paper); }
  .letterhead-wordmark { position: absolute; left: 0; right: 0; top: 17px; font-size: 7px; color: var(--brand-blue); }
  .letterhead-address { position: absolute; right: 14px; top: 14px; font-size: 3.4px; line-height: 1.5; color: var(--ink); }
  .letterhead-watermark { position: absolute; left: 0; right: 0; top: 132px; font-size: 24px; font-weight: 400; color: var(--watermark); }
  .letterhead-footer { position: absolute; left: 0; right: 0; bottom: 14px; font-size: 3.4px; line-height: 1.5; color: var(--ink); text-align: center; }

  /* envelopes */
  .envelope { width: 380px; height: 78px; background: var(--paper); overflow: hidden; }
  .envelope svg { position: absolute; inset: 0; }
  .envelope-wordmark { position: absolute; left: 0; right: 0; top: 10px; font-size: 6px; }
  .envelope-watermark { position: absolute; right: 36px; top: 34px; font-size: 12px; font-weight: 400; color: var(--watermark); }
</style>
</head>
<body>

  <!-- business card set -->
  <div class="piece card card--white" style="left:53px; top:29px;">
    <div class="wordmark">red quince</div>
    <div class="card-tagline">silk in motion</div>
    <div class="card-details">
      Dunmore Court<br>Harbor &amp; Vale<br>P.O.Box 4819<br>Carmel, CA 93921-4819<br>info@red-quince-shop.com<br>www.red-quince-shop.com
    </div>
  </div>
  <div class="label" style="left:40px; top:154px; width:88px;">business card front (1)</div>

  <div class="piece card card--navy card--centered" style="left:137px; top:29px;">
    <div class="wordmark">red quince</div>
    <div class="card-tagline">silk in motion</div>
  </div>
  <div class="label" style="left:124px; top:154px; width:88px;">business card back (1)</div>

  <div class="piece card card--navy" style="left:53px; top:216px;">
    <div class="wordmark">red quince</div>
    <div class="card-tagline">silk in motion</div>
    <div class="card-details">
      Dunmore Court<br>Harbor &amp; Vale<br>P.O.Box 4819<br>Carmel, CA 93921-4819<br>info@red-quince-shop.com<br>www.red-quince-shop.com
    </div>
  </div>
  <div class="label" style="left:40px; top:341px; width:88px;">business card front (2)</div>

  <div class="piece card card--sky card--centered" style="left:137px; top:216px;">
    <div class="wordmark">red quince</div>
    <div class="card-tagline">silk in motion</div>
  </div>
  <div class="label" style="left:124px; top:341px; width:88px;">business card back (2)</div>

  <!-- letterheads -->
  <div class="piece letterhead" style="left:247px; top:29px;">
    <div class="letterhead-wordmark wordmark">red quince</div>
    <div class="letterhead-address">Dunmore Court<br>Harbor &amp; Vale<br>P.O.Box 4819<br>Carmel, CA 93921-4819</div>
    <div class="letterhead-watermark wordmark">red quince</div>
    <div class="letterhead-footer">info@red-quince-shop.com &nbsp;·&nbsp; www.red-quince-shop.com</div>
  </div>
  <div class="label" style="left:247px; top:362px; width:245px;">letterhead option A</div>

  <div class="piece letterhead" style="left:518px; top:29px;">
    <div class="letterhead-wordmark wordmark">red quince</div>
    <div class="letterhead-watermark wordmark">red quince</div>
    <div class="letterhead-footer">Dunmore Court · Harbor &amp; Vale · P.O.Box 4819 · Carmel, CA 93921-4819<br>info@red-quince-shop.com &nbsp;·&nbsp; www.red-quince-shop.com</div>
  </div>
  <div class="label" style="left:518px; top:362px; width:245px;">letterhead option B</div>

  <!-- envelopes -->
  <div class="piece envelope" style="left:797px; top:108px;">
    <svg width="380" height="78" viewBox="0 0 380 78"><polygon points="0,0 380,0 190,34" fill="var(--navy)"/></svg>
    <div class="envelope-wordmark wordmark" style="color:var(--paper);">red quince</div>
  </div>
  <div class="piece envelope" style="left:797px; top:165px;">
    <svg width="380" height="78" viewBox="0 0 380 78"><rect width="380" height="22" fill="var(--sky)"/><polygon points="0,22 380,22 190,40" fill="var(--sky)"/></svg>
    <div class="envelope-wordmark wordmark" style="color:var(--navy);">red quince</div>
  </div>
  <div class="piece envelope" style="left:797px; top:226px;">
    <svg width="380" height="78" viewBox="0 0 380 78"><polyline points="0,0 190,34 380,0" fill="none" stroke="var(--paper-shade)" stroke-width="1.5"/></svg>
  </div>
  <div class="piece envelope" style="left:797px; top:280px;">
    <svg width="380" height="78" viewBox="0 0 380 78"><polyline points="0,0 190,30 380,0" fill="none" stroke="var(--paper-shade)" stroke-width="1.5"/></svg>
    <div class="envelope-watermark wordmark">red quince</div>
  </div>
  <div class="label" style="left:797px; top:362px; width:380px;">envelope options (4)</div>

</body>
</html>
```